Low Marsh Guild - Lanterns Over Snow Artwork

I'm looking for artwork for our latest single "Lanterns over Snow". I'm looking for hi-res jpg files for use on our website, friendwall, tunecrate and echovale sites.
Check out our previous work for reference:
www.lowmarshguild.example
https://www.videoplace.example/channel/QXT8--lomirBensKqa-YHd4r
https://www.friendwall.example/lowmarshguild/
https://tunecrate.example/low-marsh-guild

Target Market(s)

Indie music (e.g. Tillers / Mend Fans)

Industry/Entity Type

Music Download

Requirements
Must have
• - the Low Marsh Guild logo
• - the song title Lanterns Over Snow
Should not have
• - no direct Christmas imagery

```html
<!DOCTYPE html>
<html lang="en">
<head>
<meta charset="utf-8">
<title>Low Marsh Guild – Lanterns over Snow</title>
<link rel="stylesheet" href="https://fonts.googleapis.com/css2?family=Antonio:wght@400&family=Dancing+Script:wght@500&display=swap">
<style>
  :root {
    --night-top: #41444c;
    --night-mid: #1e1f25;
    --night-deep: #0a0a0d;
    --ink-wash: #8a8c92;
    --frame-blue: #2c3140;
    --snow-grey: #6a6d75;
    --snow-shadow: #2a2c32;
    --window-glow: #d97c88;
    --window-core: #f3dde0;
    --title-blush: #f4e8ea;
    --logo-white: #ffffff;
  }
  html, body {
    margin: 0;
    padding: 0;
    width: 1200px;
    height: 1200px;
    overflow: hidden;
    background: var(--night-deep);
  }
  .cover {
    position: relative;
    width: 1200px;
    height: 1200px;
    overflow: hidden;
  }
  .cover-scene {
    position: absolute;
    inset: 0;
    width: 1200px;
    height: 1200px;
    display: block;
  }
  .song-title {
    position: absolute;
    left: 650px;
    top: 92px;
    width: 470px;
    margin: 0;
    color: var(--title-blush);
    font-family: "Dancing Script", cursive;
    font-weight: 500;
    text-align: center;
    line-height: 1;
  }
  .song-title-main {
    display: block;
    font-size: 116px;
    letter-spacing: 1px;
  }
  .song-title-sub {
    display: block;
    margin-top: 2px;
    font-size: 92px;
  }
  .band-name {
    position: absolute;
    left: 478px;
    top: 786px;
    margin: 0;
    color: var(--logo-white);
    font-family: "Antonio", sans-serif;
    font-weight: 400;
    font-size: 108px;
    line-height: 116px;
    letter-spacing: 4px;
    text-transform: uppercase;
  }
  .band-name span {
    display: block;
  }
</style>
</head>
<body>
  <main class="cover">
    <svg class="cover-scene" viewBox="0 0 1200 1200" role="img" aria-label="Painted night scene: a snow-covered A-frame cabin and a long roof hung with icicles, windows glowing soft pink, deep snow in the foreground under a dark ink-splashed sky">
      <defs>
        <linearGradient id="nightBase" x1="0" y1="0" x2="0" y2="1">
          <stop offset="0" stop-color="var(--night-top)"/>
          <stop offset="0.4" stop-color="var(--night-mid)"/>
          <stop offset="0.7" stop-color="var(--night-deep)"/>
          <stop offset="1" stop-color="var(--snow-shadow)"/>
        </linearGradient>
        <radialGradient id="inkWash">
          <stop offset="0" stop-color="var(--ink-wash)" stop-opacity="0.7"/>
          <stop offset="1" stop-color="var(--ink-wash)" stop-opacity="0"/>
        </radialGradient>
        <radialGradient id="frameTone">
          <stop offset="0" stop-color="var(--frame-blue)" stop-opacity="0.9"/>
          <stop offset="1" stop-color="var(--frame-blue)" stop-opacity="0"/>
        </radialGradient>
        <radialGradient id="windowWarmth">
          <stop offset="0" stop-color="var(--window-core)" stop-opacity="0.85"/>
          <stop offset="0.35" stop-color="var(--window-glow)" stop-opacity="0.7"/>
          <stop offset="1" stop-color="var(--window-glow)" stop-opacity="0"/>
        </radialGradient>
        <radialGradient id="snowDrift">
          <stop offset="0" stop-color="var(--snow-grey)" stop-opacity="0.9"/>
          <stop offset="1" stop-color="var(--snow-grey)" stop-opacity="0"/>
        </radialGradient>
      </defs>
      <rect width="1200" height="1200" fill="url(#nightBase)"/>
      <ellipse cx="560" cy="90" rx="380" ry="170" fill="url(#inkWash)"/>
      <ellipse cx="170" cy="380" rx="260" ry="420" fill="url(#frameTone)"/>
      <ellipse cx="920" cy="380" rx="360" ry="90" fill="url(#inkWash)" opacity="0.45"/>
      <ellipse cx="135" cy="595" rx="150" ry="120" fill="url(#windowWarmth)"/>
      <ellipse cx="708" cy="590" rx="110" ry="130" fill="url(#windowWarmth)"/>
      <ellipse cx="995" cy="590" rx="130" ry="140" fill="url(#windowWarmth)"/>
      <ellipse cx="200" cy="1000" rx="420" ry="240" fill="url(#snowDrift)"/>
      <ellipse cx="1080" cy="1080" rx="260" ry="180" fill="url(#snowDrift)" opacity="0.8"/>
    </svg>

    <h1 class="song-title">
      <span class="song-title-main">Lanterns</span>
      <span class="song-title-sub">over Snow</span>
    </h1>

    <p class="band-name" aria-label="Low Marsh Guild">
      <span>Low</span>
      <span>Marsh</span>
      <span>Guild</span>
    </p>
  </main>
</body>
</html>
```